New Website Design (Uncoded) Competition for Lorvex Trade Link

Please submit design concepts for a Joomla 3.0 Website for LORVEX TRADE LINK company. Our client prefers a modem style design, responsive to all mobile devices,
The website demo content needs to be clear and detailed.

Menu sample:
Home/About Us/Service/Strength/Partner/News/Contact US/Blog

Requirements:
1. Only need to submit the PSD for the design, coding work is not included.
2. Please submit both Homepage and Inner page to demonstrate the concept.
3. The Homepage needs to include: LOGO/MENU/Banner/Language Switcher/Company Introduction/Welcome module/Advertising Module/Footer Menu/Footer/Copyright/Social Links
4. Use Asian business women for demo pictures/Could try city pictures for background.
5. Prefer SINGLE SCREEN design rather than scrollable multiple screen designs.
6. Avoid any chain symbol since the company is more about financial business.
7. Avoid any direct connotations related with money or cash.
Updates

Hi Designers, I have clearly state the requirements that avoid using neg connontation pictures like cash/ property, though still receive concepts like that. Please check the brief clearly and mark at Update with "cheers" Kel from VT

Target Market(s)

Dongrui Lorvex Trade link Company provide cross-border Supply chain Financial service by integrating Dongrui Trade Link resource.
The Company mission is become the most respectful, professional and valuable Chinese Supply Chain Financial Company, pioneer the supply chain industry.

Industry/Entity Type

Financial

Font styles to use
Sans Serif

Colors
33b7a4

Requirements
Must have
• 1. Necessary Web element, including Logo/navigation/ Banner/ Footer
2. Asia business Women pictures.
Should not have
• 6. Avoid any chain symbol since the company is more about financial business.

```html
<!DOCTYPE html>
<html lang="en">
<head>
<meta charset="utf-8">
<title>Lorvex Trade Link</title>
<link href="https://fonts.googleapis.com/css2?family=Cinzel:wght@700&family=Raleway:wght@300;500;600&family=Source+Sans+3:wght@400;600&display=swap" rel="stylesheet">
<style>
:root{
  --brand-blue:#1b7cc4;
  --brand-grey:#5a5a5a;
  --ink:#222;
  --text:#333;
  --nav-ink:#2b2b2b;
  --teal-dark:#2f8a80;
  --teal-light:#6fbfae;
  --footer-bg:#3e3e3e;
  --footer-ink:#ffffff;
  --ad-lime:#c9d32a;
  --ad-olive:#b3b400;
  --ad-ink:#3b3b3b;
  --button-gold:#f3c21a;
}
*{margin:0;padding:0;box-sizing:border-box}
html,body{width:1088px;height:1200px;overflow:hidden;background:#fff}
body{position:relative;font-family:Arial,Helvetica,sans-serif;color:var(--text)}
.abs{position:absolute}

/* header */
.site-header{position:absolute;left:0;top:0;width:1088px;height:111px;background:#fff;box-shadow:0 1px 3px rgba(0,0,0,.12);z-index:2}
.logo{position:absolute;left:93px;top:18px;display:flex;align-items:center;gap:12px}
.logo-mark{width:50px;height:50px;background:var(--brand-blue);border-radius:4px}
.logo-name{font-family:"Source Sans 3",sans-serif;font-weight:600;color:var(--brand-grey);line-height:1}
.logo-name .l1{display:block;font-size:38px;letter-spacing:1px}
.logo-name .l2{display:block;font-size:19px;letter-spacing:2.5px;margin-top:6px}
.lang-select{position:absolute;left:838px;top:18px;width:158px;height:28px;border:1px solid #d4d4d4;border-radius:3px;background:linear-gradient(#fff,#f1f1f1);font-size:11.5px;color:#555;padding:7px 0 0 7px}
.lang-select .arrow{position:absolute;right:5px;top:5px;width:18px;height:17px;border:1px solid #c8c8c8;background:#fff}
.lang-select .arrow svg{position:absolute;left:4px;top:5px}
.main-nav{position:absolute;top:67px;right:92px;display:flex;gap:26px;font-family:"Source Sans 3",sans-serif;font-size:14.5px;color:var(--nav-ink)}
.main-nav a{color:inherit;text-decoration:none;position:relative;padding:0 4px}
.main-nav a.active::after{content:"";position:absolute;left:0;right:0;top:24px;height:3px;background:var(--brand-blue)}

/* hero */
.hero{position:absolute;left:0;top:111px;width:1088px;height:488px;background:linear-gradient(180deg,#5eae9e 0%,#4f9e8f 45%,#3d8c80 100%)}
.hero-photo{position:absolute;left:95px;top:20px;width:408px;height:468px;background:linear-gradient(180deg,rgba(40,60,60,.25),rgba(20,30,35,.55));border-radius:160px 160px 0 0}
.hero-title{position:absolute;left:522px;top:170px;font-family:Cinzel,serif;font-weight:700;font-size:40px;color:#fff;letter-spacing:.5px}
.hero-text{position:absolute;left:522px;top:226px;width:480px;font-size:15.5px;line-height:20px;color:#fff}
.btn-read{position:absolute;left:522px;top:323px;width:120px;height:38px;border:2px solid #fff;border-radius:5px;background:linear-gradient(#3a95d6,#1a72b9);color:#fff;font-family:Georgia,serif;font-size:19px;text-align:center;line-height:33px}

/* welcome */
.section-title{position:absolute;font-family:Cinzel,serif;font-weight:700;font-size:25px;color:var(--brand-blue);letter-spacing:.3px}
.welcome-title{left:90px;top:638px}
.intro-lead{position:absolute;left:93px;top:694px;width:510px;font-size:13.5px;line-height:19px;font-weight:bold;color:var(--ink)}
.intro-body{position:absolute;left:93px;top:750px;width:505px;font-size:13.3px;line-height:19px;color:var(--text)}
.team-photo{position:absolute;left:668px;top:624px;width:321px;height:260px;background:linear-gradient(180deg,#f4f5f6 0%,#5a5f66 40%,#2d3036 100%);border-radius:140px 140px 0 0}

/* advertising */
.ad-title{left:88px;top:885px}
.ad-banner{position:absolute;left:93px;top:934px;width:896px;height:152px;border:2px solid #dcdcdc;border-radius:5px;overflow:hidden;background:linear-gradient(90deg,#c2c819 0%,#d3d91e 25%,#b6b600 60%,#a9ad00 100%)}
.ad-photo{position:absolute;right:0;top:0;width:300px;height:152px;background:linear-gradient(90deg,#e2e6e6,#f7f8f8);clip-path:polygon(25% 0,100% 0,100% 100%,0 100%)}
.ad-line1{position:absolute;left:45px;top:14px;font-family:Raleway,sans-serif;font-weight:300;font-size:30px;color:#fff}
.ad-line2{position:absolute;left:45px;top:46px;font-family:Raleway,sans-serif;font-weight:600;font-size:48px;color:var(--ad-ink);letter-spacing:.5px}
.ad-line3{position:absolute;left:213px;top:104px;font-family:Raleway,sans-serif;font-weight:300;font-size:30px;color:#fff}
.btn-more{position:absolute;left:459px;top:106px;width:162px;height:34px;background:var(--button-gold);border:1px solid #e0a800;font-family:Raleway,sans-serif;font-weight:600;font-size:19px;color:var(--ad-ink);text-align:center;line-height:32px}

/* footer */
.site-footer{position:absolute;left:0;top:1104px;width:1088px;height:96px;background:var(--footer-bg);color:var(--footer-ink)}
.footer-nav{position:absolute;left:96px;top:24px;font-family:"Source Sans 3",sans-serif;font-size:11.5px;display:flex;gap:6px}
.footer-nav span.sep{padding:0 6px}
.copyright{position:absolute;left:97px;top:61px;font-size:12.5px}
.footer-divider{position:absolute;left:419px;top:50px;height:42px;border-left:1px dotted #777}
.social{position:absolute;left:441px;top:54px;display:flex;gap:10px}
.social span{display:block;width:26px;height:26px;border-radius:50%}
.s-a{background:#2a5a9a}.s-b{background:#2aa3e0}.s-c{background:#f18c1d}.s-d{background:#9c9c9c;position:relative}
.s-d svg{position:absolute;left:6px;top:8px}
.footer-logo{position:absolute;left:784px;top:18px;display:flex;align-items:center;gap:10px}
.footer-logo .logo-mark{width:44px;height:44px;background:#9a9a9a}
.footer-logo .logo-name{color:#d8d8d8}
.footer-logo .l1{font-size:34px}
.footer-logo .l2{font-size:17px;margin-top:5px}
</style>
</head>
<body>

<header class="site-header">
  <div class="logo">
    <span class="logo-mark"></span>
    <span class="logo-name"><span class="l1">LORVEX</span><span class="l2">TRADE LINK</span></span>
  </div>
  <div class="lang-select">Select your Language
    <span class="arrow"><svg width="9" height="6" viewBox="0 0 9 6"><path d="M0 0h9L4.5 6z" fill="#1b7cc4"/></svg></span>
  </div>
  <nav class="main-nav">
    <a class="active">Home</a><a>About Us</a><a>Service</a><a>Strength</a><a>Partner</a><a>News</a><a>Contact US</a><a>Blog</a>
  </nav>
</header>

<section class="hero" role="img" aria-label="Business woman in a dark suit presenting with an open hand, city skyline in teal tones behind">
  <div class="hero-photo"></div>
  <h1 class="hero-title">LOREM IPSUM DOLOR</h1>
  <p class="hero-text">Duis aute irure dolor in reprehenderit in voluptate velit esse cillum dolore eu fugiat nulla pariatur. Excepteur sint occaecat cupidatat non proident, sunt in culpa qui officia deserunt mollit anim id est laborum.</p>
  <a class="btn-read">Read More</a>
</section>

<h2 class="section-title welcome-title">WELCOME TO LORVEX TRADE LINK</h2>
<p class="intro-lead">Lorem ipsum dolor sit amet, consectetur adipiscing elit, sed do eiusmod tempor incididunt ut labore</p>
<p class="intro-body">et dolore magna aliqua. Ut enim ad minim veniam, quis nostrud exercitation ullamco laboris nisi ut aliquip ex ea commodo consequat. Duis aute irure dolor in reprehenderit in voluptate velit esse cillum dolore eu fugiat nulla pariatur. Excepteur sint occaecat cupidatat non proident, sunt in culpa qui officia deserunt mollit anim id est laborum...</p>
<div class="team-photo" role="img" aria-label="Group of smiling business people in suits"></div>

<h2 class="section-title ad-title">ADVERTISING MODULE</h2>
<div class="ad-banner">
  <div class="ad-photo" role="img" aria-label="Business man drawing a rising growth chart on a white wall"></div>
  <div class="ad-line1">Focus on your core</div>
  <div class="ad-line2">business &amp; call</div>
  <div class="ad-line3">a land experts.</div>
  <a class="btn-more">More Details..</a>
</div>

<footer class="site-footer">
  <nav class="footer-nav">
    <span>Home</span><span class="sep">/</span><span>About Us</span><span class="sep">/</span><span>Service</span><span class="sep">/</span><span>Strength</span><span class="sep">/</span><span>Partner</span><span class="sep">/</span><span>News</span><span class="sep">/</span><span>Contact US</span><span class="sep">/</span><span>Blog</span>
  </nav>
  <p class="copyright">Copyright © 2014 All Rights Reserved | Privacy Policy</p>
  <span class="footer-divider"></span>
  <div class="social">
    <span class="s-a" aria-label="Social link"></span>
    <span class="s-b" aria-label="Social link"></span>
    <span class="s-c" aria-label="Feed link"></span>
    <span class="s-d" aria-label="Email"><svg width="14" height="10" viewBox="0 0 14 10"><rect x=".5" y=".5" width="13" height="9" fill="#fff" stroke="#9c9c9c"/><path d="M.5 .5L7 5.5 13.5 .5" fill="none" stroke="#9c9c9c"/></svg></span>
  </div>
  <div class="footer-logo">
    <span class="logo-mark"></span>
    <span class="logo-name"><span class="l1">LORVEX</span><span class="l2">TRADE LINK</span></span>
  </div>
</footer>

</body>
</html>
```